Business Card Design needed - Something Awesome!

Need a business card designed. Company is "Harbor Vane Consulting" we do consulting and also have sales automation technology.
I'm going to use thick stock or metal, something really nice... I was thinking about a QR Code on the back that would just upload my contact info to the persons contact, etc -

This is a Strategy Company with a tech feel. I'm open to ideas but really want this to be nice!

I need a template that should include:

Name | Position or Title
D: 555.203.8146
www.harborvaneconsulting.example

I'm going to attach my contact so you can use that one, I need to get this printed.

Target Market(s)

Small to mid size customers, Entrepreneurs etc.

Industry/Entity Type

Consulting, Tech, Private Equity.

Contact Information for Business Card

Name, Phone, Maybe email, URL

Font styles to use
Sans Serif

Colors

Designer to choose only greyscale colors for use in the design.

Requirements
Must have
• Fresh, Clean, stand out from the crowd - will be on thick stock or metal.
Nice to have
• Clean, simple yet impactful.
Should not have
• Not cartoonish

```html
<!DOCTYPE html>
<html lang="en">
<head>
<meta charset="utf-8">
<title>Harbor Vane Consulting – Business Card</title>
<link href="https://fonts.googleapis.com/css2?family=Montserrat:wght@400;500;600;700&display=swap" rel="stylesheet">
<style>
  :root {
    --backdrop: #d9d9d9;
    --card-black: #1f1f1f;
    --card-black-hi: #3a3a3a;
    --card-white: #ffffff;
    --ink: #111111;
    --ink-soft: #6b6b6b;
    --ink-on-dark: #e6e6e6;
    --rule: #1a1a1a;
  }
  * { margin: 0; padding: 0; box-sizing: border-box; }
  html, body {
    width: 1200px; height: 987px; overflow: hidden;
    background: var(--backdrop);
    font-family: "Montserrat", sans-serif;
  }
  .canvas { position: relative; width: 1200px; height: 987px; }

  .card {
    position: absolute;
    width: 600px; height: 343px;
    border-radius: 3px;
    box-shadow: 0 10px 28px rgba(0,0,0,.22);
    overflow: hidden;
  }

  /* Back side */
  .card-back {
    left: 130px; top: 130px;
    background: radial-gradient(ellipse at 50% 25%, var(--card-black-hi), var(--card-black) 70%);
    color: var(--ink-on-dark);
    display: flex; flex-direction: column; align-items: center;
  }
  .card-back .brand {
    margin-top: 118px;
    display: flex; align-items: center; gap: 14px;
    font-size: 22px; font-weight: 600; letter-spacing: .5px;
    color: var(--ink-on-dark);
  }
  .brand-square { width: 18px; height: 18px; background: var(--ink-on-dark); flex: none; }
  .card-back .url {
    margin-top: auto; margin-bottom: 42px;
    font-size: 15px; font-weight: 500; letter-spacing: .3px;
  }

  /* Front side */
  .card-front {
    left: 470px; top: 500px;
    background: var(--card-white);
    display: flex; align-items: center;
  }
  .front-brand {
    width: 262px; flex: none; padding-left: 26px;
    display: flex; align-items: center; gap: 9px;
    font-size: 15px; font-weight: 700; color: var(--ink);
    white-space: nowrap;
  }
  .front-brand .brand-square { width: 14px; height: 14px; background: var(--ink); }
  .divider {
    width: 2px; height: 215px; background: var(--rule); flex: none;
    margin-right: 22px;
  }
  .contact { color: var(--ink-soft); min-width: 0; padding-right: 20px; }
  .contact .name { font-size: 22px; font-weight: 600; color: var(--ink); line-height: 1.1; }
  .contact .title { font-size: 14px; margin-top: 3px; }
  .contact .address { font-size: 14px; line-height: 1.4; margin-top: 16px; }
  .contact ul { list-style: none; margin-top: 16px; font-size: 13.5px; line-height: 1.45; }
  .contact li { display: flex; align-items: center; gap: 9px; white-space: nowrap; }
  .contact li svg { width: 12px; height: 12px; flex: none; }
</style>
</head>
<body>
<div class="canvas">

  <section class="card card-back" aria-label="Business card back">
    <div class="brand"><span class="brand-square"></span>Harbor Vane Consulting</div>
    <p class="url">www.harborvaneconsulting.example</p>
  </section>

  <section class="card card-front" aria-label="Business card front">
    <div class="front-brand"><span class="brand-square"></span>Harbor Vane Consulting</div>
    <div class="divider"></div>
    <div class="contact">
      <p class="name">Daniel Reyes</p>
      <p class="title">President</p>
      <p class="address">Street Name Avenue, Suite 100<br>State, Zip Code, Country</p>
      <ul>
        <li>
          <svg viewBox="0 0 16 16" aria-hidden="true"><path fill="#111" d="M3.6 1.2l2.3 2.6-1.2 1.9c.9 2 2.6 3.7 4.6 4.6l1.9-1.2 2.6 2.3-1.3 2.6C7.2 13.9 2.1 8.8 1 3.1z"/></svg>
          555.203.8146
        </li>
        <li>
          <svg viewBox="0 0 16 16" aria-hidden="true"><rect x="4" y="1" width="8" height="14" rx="1.5" fill="none" stroke="#111" stroke-width="1.6"/><rect x="7" y="12" width="2" height="1.4" fill="#111"/></svg>
          555.203.8170
        </li>
        <li>
          <svg viewBox="0 0 16 16" aria-hidden="true"><rect x="1" y="3.5" width="14" height="9" fill="#111"/><path d="M1.5 4l6.5 5 6.5-5" fill="none" stroke="#fff" stroke-width="1.2"/></svg>
          info@harborvaneconsulting.example
        </li>
        <li>
          <svg viewBox="0 0 16 16" aria-hidden="true"><g fill="none" stroke="#111" stroke-width="1.3"><circle cx="8" cy="8" r="6.5"/><ellipse cx="8" cy="8" rx="2.8" ry="6.5"/><path d="M1.5 8h13M2.5 4.8h11M2.5 11.2h11"/></g></svg>
          harborvaneconsulting.example
        </li>
      </ul>
    </div>
  </section>

</div>
</body>
</html>
```